Elegant, Playful, Health And Wellness Packaging Design for an Essential Oil Diffuser

Box design for diffuser, should be elegant, luxury, white box with gold foil and vibrant color combination that pops off the white box.

Designs look the same

```html
<!DOCTYPE html>
<html lang="en">
<head>
<meta charset="utf-8">
<title>Aurelle Sola Ultrasonic Diffuser – Box Dieline</title>
<link rel="stylesheet" href="https://fonts.googleapis.com/css2?family=Cinzel:wght@400;700&family=Carlito:wght@400;700&family=Uncial+Antiqua&display=swap">
<style>
  :root {
    --paper: #ffffff;
    --navy: #03061c;
    --cocoa: #3a1512;
    --ink: #1b1b2e;
    --swirl-light: #f1ecec;
    --swirl-lilac: #f3eef8;
    --ornament: #1a1a1a;
  }
  * { box-sizing: border-box; margin: 0; padding: 0; }
  html, body {
    width: 1200px; height: 738px; overflow: hidden;
    background: var(--paper);
  }
  .dieline { position: relative; width: 1200px; height: 738px; }

  /* Lid (printed upside down) */
  .lid {
    position: absolute; left: 385px; top: 62px; width: 150px; height: 165px;
    transform: rotate(180deg);
  }
  .lid .flourish {
    position: absolute; left: 10px; width: 116px; height: 20px;
    background: linear-gradient(90deg, #e6e6e6, #bdbdbd 50%, #e6e6e6);
    border-radius: 10px;
  }
  .lid .flourish.top { top: 0; }
  .lid .flourish.bottom { bottom: 0; }
  .lid .seal {
    position: absolute; left: 43px; top: 36px; width: 64px; height: 64px;
    border-radius: 50%; background: var(--ornament);
  }
  .lid .brand {
    position: absolute; left: 0; top: 108px; width: 150px; text-align: center;
    font-family: "Cinzel", serif; font-weight: 700; font-size: 22px;
    letter-spacing: 1px; color: var(--ornament);
  }

  /* Side panels */
  .panel {
    position: absolute; top: 303px; width: 295px; height: 236px;
    overflow: hidden; background: var(--paper);
  }
  .panel.back-left { left: 11px; }
  .panel.front { left: 305px; }
  .panel.info { left: 600px; }
  .panel.side-right { left: 894px; }

  .swirl {
    position: absolute; left: 0; top: 0; width: 295px; height: 140px;
    background:
      radial-gradient(ellipse at 15% 40%, var(--swirl-light) 0 35%, transparent 60%),
      radial-gradient(ellipse at 85% 40%, var(--swirl-light) 0 35%, transparent 60%),
      radial-gradient(ellipse at 50% 90%, var(--swirl-lilac) 0 20%, transparent 50%);
  }
  .wave { position: absolute; left: 0; top: 0; width: 295px; height: 236px; }
  .wave path { fill: var(--navy); }

  .tagline {
    position: absolute; left: 0; top: 15px; width: 100%; text-align: center;
    font-family: "Cinzel", serif; font-weight: 700; font-size: 9.6px;
    color: var(--ink); letter-spacing: 0.2px;
  }
  .seal {
    position: absolute; left: 115px; top: 40px; width: 65px; height: 65px;
    border-radius: 50%; background: var(--cocoa);
  }
  .brand {
    position: absolute; left: 0; top: 104px; width: 100%; text-align: center;
    font-family: "Cinzel", serif; font-weight: 700; font-size: 23px;
    line-height: 1; color: var(--cocoa); letter-spacing: 1px;
  }
  .collection {
    position: absolute; left: 0; top: 129px; width: 100%; text-align: center;
    font-family: "Cinzel", serif; font-size: 8px; color: var(--cocoa);
  }
  .product {
    position: absolute; left: 0; top: 150px; width: 100%; text-align: center;
    font-family: "Uncial Antiqua", serif; font-size: 33px; line-height: 1;
    color: var(--cocoa); letter-spacing: 4px;
  }
  .footer-line {
    position: absolute; left: 0; top: 209px; width: 100%; text-align: center;
    font-family: "Cinzel", serif; font-size: 9.4px; color: #ffffff;
    letter-spacing: 0.6px;
  }
  .footer-line.url { font-family: "Crimson Text", "Times New Roman", serif; letter-spacing: 0.2px; }

  /* Info panel */
  .info h2 {
    position: absolute; left: 0; top: 13px; width: 100%; text-align: center;
    font-family: "Cinzel", serif; font-weight: 400; font-size: 11px;
    color: var(--ink);
  }
  .info .blurb {
    position: absolute; left: 12px; top: 31px; width: 271px;
    font-family: "Carlito", sans-serif; font-weight: 700; font-size: 8.2px;
    line-height: 10.4px; text-align: justify; color: var(--cocoa);
  }
  .info .list {
    position: absolute; top: 92px; list-style: none;
    font-family: "Carlito", sans-serif; font-weight: 700; font-size: 8.2px;
    color: var(--cocoa);
  }
  .info .list.features { left: 15px; }
  .info .list.specs { left: 152px; }
  .info .list .heading { padding-left: 14px; margin-bottom: 9px; }
  .info .list li.item {
    position: relative; padding-left: 14px; height: 13px; line-height: 13px;
  }
  .info .list li.item::before {
    content: "★"; position: absolute; left: 0; top: 0; font-size: 9px;
  }
  .info .list li.cont { padding-left: 14px; height: 13px; line-height: 13px; }
</style>
</head>
<body>
<main class="dieline">

  <section class="lid" aria-label="Box lid">
    <div class="flourish top" role="img" aria-label="Decorative scroll flourish"></div>
    <div class="seal" aria-hidden="true"></div>
    <div class="brand">AURELLE</div>
    <div class="flourish bottom" role="img" aria-label="Decorative scroll flourish"></div>
  </section>

  <section class="panel back-left">
    <div class="swirl" role="img" aria-label="Faint floral swirl and leaf ornament"></div>
    <svg class="wave" viewBox="0 0 295 236" aria-hidden="true"><path d="M0 153 C55 200 140 218 295 153 L295 236 L0 236 Z"/></svg>
    <div class="seal" aria-hidden="true"></div>
    <div class="brand">AURELLE</div>
    <div class="collection">SIGNATURE RARE OILS COLLECTION</div>
    <div class="product">SOLA</div>
    <div class="footer-line url">-Website url: www.aurelle-oils.com</div>
  </section>

  <section class="panel front">
    <div class="swirl" role="img" aria-label="Faint floral swirl and leaf ornament"></div>
    <svg class="wave" viewBox="0 0 295 236" aria-hidden="true"><path d="M0 153 C55 200 140 218 295 153 L295 236 L0 236 Z"/></svg>
    <div class="tagline">EXPERIENCE THE ESSENCE OF NATURE</div>
    <div class="seal" aria-hidden="true"></div>
    <div class="brand">AURELLE</div>
    <div class="collection">SIGNATURE RARE OILS COLLECTION</div>
    <div class="product">SOLA</div>
    <div class="footer-line">ULTRASONIC DIFFUSER</div>
  </section>

  <section class="panel info">
    <h2>AURELLE RARE ESSENTIAL OILS DIFFUSER</h2>
    <p class="blurb">Experience the pure essence of nature with the Rare Oils Sola Diffuser. Sourced from the farthest reaches of the earth, Aurelle Rare Oils are extracted only from the highest quality and purest raw form ingredients. Using the Sola diffuser with Aurelle Rare Oils can help improve health, quality of life, and overall spiritual balance.</p>
    <ul class="list features">
      <li class="heading">Features :</li>
      <li class="item">Continuous diffusing</li>
      <li class="item">Timer settings</li>
      <li class="item">7 LED color &amp; light settings</li>
      <li class="item">Portable</li>
      <li class="item">Pet safe</li>
      <li class="item">Easy to clean</li>
    </ul>
    <ul class="list specs">
      <li class="heading">Specifications :</li>
      <li class="item">Dimensions : 135*135*108 mm</li>
      <li class="item">Capacity : 300 ml</li>
      <li class="item">33 ml / hour output</li>
      <li class="item">Safety Auto-off when Empty</li>
      <li class="item">Whisper Quiet</li>
      <li class="item">Contains 1 SOLA Diffuser,</li>
      <li class="cont">1 Power Adaptor</li>
    </ul>
  </section>

  <section class="panel side-right">
    <div class="swirl" role="img" aria-label="Faint floral swirl and leaf ornament"></div>
    <svg class="wave" viewBox="0 0 295 236" aria-hidden="true"><path d="M0 153 C55 200 140 218 295 153 L295 236 L0 236 Z"/></svg>
    <div class="tagline">EXPERIENCE THE ESSENCE OF NATURE</div>
    <div class="seal" aria-hidden="true"></div>
    <div class="brand">AURELLE</div>
    <div class="collection">SIGNATURE RARE OILS COLLECTION</div>
    <div class="product">SOLA</div>
    <div class="footer-line">ULTRASONIC DIFFUSER</div>
  </section>

</main>
</body>
</html>
```